Electrician Business Card/ company logo/small business

New Business Cards and logo needed that will catch peoples eye and say we went that extra step. Attached is a design possibly to be incorporated, if u have your own great, lets see it!... This will be a small local business. thank you for all you do!
Falcon Electric
Dov Merrick Owner
Journeyman Electrician
phone 1.482.639.2075
email: QRTFalconElectric@zentromail.com
call for free estimate!
Updates

Accepted and approved for cards

Target Market(s)

support small local business

Industry/Entity Type

Electrical,

Contact Information for Business Card

name, title,company/ logo, phone, email, free estimate

Font styles to use
Other font styles liked:
• easy to read

Colors

Designer to choose colors to be used in the design.

Requirements
Must have
• eye catching everything! logo and falcon electric listed on business card/logo, incorp logo in the background of card
Nice to have
• lightening bolts in eyes or around the triangle? vertical, modern, any design that would be unique and stand out
Should not have
• pinks, reds, yellows,brown

```html
<!DOCTYPE html>
<html lang="en">
<head>
<meta charset="utf-8">
<title>Falcon Electric – Business Card</title>
<link href="https://fonts.googleapis.com/css2?family=Arimo:wght@400;700&display=swap" rel="stylesheet">
<style>
  :root {
    --backdrop: #1c1c1d;
    --card: #0b0b0c;
    --card-edge: #1a1a1b;
    --blue: #1b8ad8;
    --blue-deep: #1466b3;
    --white: #f2f2f2;
    --silver: #bfc2c6;
    --divider: #3a3a3c;
  }
  * { box-sizing: border-box; margin: 0; padding: 0; }
  html, body {
    width: 1200px; height: 900px; overflow: hidden;
    background: var(--backdrop);
    font-family: "Arimo", Arial, sans-serif;
  }
  .sheet {
    width: 1200px; height: 900px;
    display: flex; flex-direction: column;
    align-items: center; justify-content: center; gap: 56px;
  }
  .card {
    width: 660px; height: 377px;
    background: var(--card);
    border-radius: 22px;
    border: 1px solid var(--card-edge);
    position: relative;
    overflow: hidden;
  }
  /* Front */
  .card-front { display: flex; align-items: center; }
  .brand-block {
    width: 270px; height: 100%;
    display: flex; flex-direction: column; align-items: center; justify-content: center; gap: 18px;
  }
  .brand-dot {
    width: 96px; height: 96px; border-radius: 50%;
    background: var(--blue);
  }
  .brand-name {
    color: var(--blue);
    font-weight: 700; font-size: 26px; letter-spacing: 2px;
    text-transform: uppercase; text-align: center; line-height: 1.15;
  }
  .divider {
    width: 1px; height: 220px; background: var(--divider);
  }
  .details { padding-left: 42px; }
  .person-name {
    color: var(--blue);
    font-weight: 700; font-size: 34px; text-transform: uppercase; letter-spacing: 0.5px;
  }
  .person-title {
    color: var(--white); font-size: 20px; margin-top: 4px;
  }
  .contact-list { list-style: none; margin-top: 30px; }
  .contact-list li {
    display: flex; align-items: center; gap: 12px;
    color: var(--white); font-size: 17px; margin-bottom: 9px;
  }
  .contact-icon { width: 18px; height: 18px; flex: none; }
  /* Back */
  .card-back {
    display: flex; align-items: center; justify-content: center; gap: 26px;
  }
  .card-back .brand-dot { background: var(--silver); width: 110px; height: 110px; }
  .card-back .brand-name { color: var(--silver); font-size: 34px; text-align: left; }
</style>
</head>
<body>
<main class="sheet">
  <section class="card card-front">
    <div class="brand-block">
      <span class="brand-dot"></span>
      <span class="brand-name">Falcon<br>Electric</span>
    </div>
    <div class="divider"></div>
    <div class="details">
      <h1 class="person-name">Dov Merrick</h1>
      <p class="person-title">Journeyman Electrician</p>
      <ul class="contact-list">
        <li>
          <svg class="contact-icon" viewBox="0 0 24 24" fill="none" stroke="var(--blue)" stroke-width="2.2" stroke-linecap="round" stroke-linejoin="round"><path d="M22 16.9v3a2 2 0 0 1-2.2 2 19.8 19.8 0 0 1-8.6-3.1 19.5 19.5 0 0 1-6-6A19.8 19.8 0 0 1 2.1 4.2 2 2 0 0 1 4.1 2h3a2 2 0 0 1 2 1.7c.1 1 .4 1.9.7 2.8a2 2 0 0 1-.5 2.1L8 9.9a16 16 0 0 0 6 6l1.3-1.3a2 2 0 0 1 2.1-.4c.9.3 1.8.6 2.8.7a2 2 0 0 1 1.7 2z"/></svg>
          1.482.639.2075
        </li>
        <li>
          <svg class="contact-icon" viewBox="0 0 24 24"><rect x="2" y="5" width="20" height="14" rx="1.5" fill="var(--blue)"/><path d="M2.5 6l9.5 7 9.5-7" fill="none" stroke="var(--card)" stroke-width="1.8"/></svg>
          QRTFalconElectric@zentromail.com
        </li>
        <li>
          <svg class="contact-icon" viewBox="0 0 24 24" fill="none" stroke="var(--blue)" stroke-width="2"><circle cx="12" cy="12" r="10"/><path d="M2 12h20M12 2c3 3 3 17 0 20M12 2c-3 3-3 17 0 20"/></svg>
          www.falconelectricpro.com
        </li>
      </ul>
    </div>
  </section>

  <section class="card card-back">
    <span class="brand-dot"></span>
    <span class="brand-name">Falcon<br>Electric</span>
  </section>
</main>
</body>
</html>
```